Wix site for a family history research service / genealogist

Design a Wix website for a genealogy/family history research business.

The colour scheme and logo exist and the main imagery has been selected and purchased. The main emotion I'd like the website to convey is "looking up" - like looking up your family tree, looking up a DNA helix, looking up to your parents, grandparents etc. I want the vibe to be one that is enthusiastic about the potential discoveries in your family's history you can make on my website. My service is to the general public, but the main target group are older people 50+ in Australia (I advertise in retirement homes, on golf courses etc.).
I'd like the website to be
- friendly, warm, approachable, trustworthy and open in terms of it's feel
- easy to read, understand and navigate for older people (this is important)
- feature a "language switch" that allows for 3 languages. Ideally pre-selected by geographic origin of visitor.
- Show clear pathways to action (contact or purchase)
- Has a simply shopping cart function that connects to PayPal

The website sections are as follows:
1. A general "Home" page or section
2. About us/me
3. Services (there will be an initial 4 products/services)
3.1 Traditional genealogy (2 products)
3.2 DNA-based ancestry tracing (2 products)
4. Case studies (initially 2)
5. Contact
(The headings are only indicative at this stage)
There is no pre-existing content yet. I'd like to work with lorem ipsum at the beginning. Some more imagery may have to be acquired, I am expecting that.
So far there is only a Facebook page https://www.examplebook.test/profile.php?id=48305716629384

Target Market(s)

Older people in Australia, more males than females

Industry/Entity Type

Personal services - Genealogy

Font styles to use
Serif
Decorative

Colors

Designer to choose colors to be used in the design.

Requirements
Must have
• Feel warm, feel trustworthy, clear call to action
Should not have
• Too small writing, confusing imagery

```html
<!DOCTYPE html>
<html lang="en">
<head>
<meta charset="utf-8">
<title>Edwin J. Harrow – Family History Research</title>
<link rel="stylesheet" href="https://fonts.googleapis.com/css2?family=Cinzel:wght@500;600;700&family=Poppins:wght@400;500&display=swap">
<style>
:root{
  --green:#0b6b2e;
  --green-bright:#00a24c;
  --cream:#f6efe5;
  --ink:#1a1a1a;
  --text:#2b2b2b;
  --white:#ffffff;
  --muted:#b9b9b9;
}
*{box-sizing:border-box;margin:0;padding:0}
html,body{width:1200px;height:3597px;overflow:hidden}
body{position:relative;background:var(--white);font-family:'Poppins',sans-serif;color:var(--text)}
.abs{position:absolute}
.serif{font-family:'Cinzel',serif}

/* header */
.site-header{left:0;top:0;width:1200px;height:71px;background:var(--green)}
.brand-badge{left:87px;top:10px;width:126px;height:106px;background:var(--white);border-radius:63px 63px 50% 50%;display:flex;flex-direction:column;align-items:center;justify-content:center;gap:6px}
.brand-dot{width:14px;height:14px;border-radius:50%;background:var(--green)}
.brand-name{font-family:'Cinzel',serif;font-weight:600;font-size:12px;color:var(--green);text-align:center;line-height:1.15}
.main-nav{top:27px;font-family:'Cinzel',serif;font-weight:500;font-size:15px;color:var(--white)}
.lang-pill{left:1045px;top:24px;width:66px;height:24px;border:1.5px solid var(--white);border-radius:12px;color:var(--white);font-size:11px;display:flex;align-items:center;justify-content:center;gap:5px}

/* hero */
.hero-bg{left:0;top:71px;width:1200px;height:746px;background:linear-gradient(100deg,#ffffff 0%,#fbf8f3 50%,var(--cream) 100%)}
.hero-deco{left:-76px;top:132px;width:150px;height:144px;border-radius:50%;background:#f3e8db}
.hero-kicker{left:89px;top:224px;font-family:'Cinzel',serif;font-size:20px;color:var(--green)}
.hero-title{left:89px;top:246px;font-family:'Cinzel',serif;font-weight:700;font-size:67px;line-height:74px;color:var(--ink)}
.hero-copy{left:89px;top:409px;width:460px;font-size:14px;line-height:20px;color:var(--ink)}
.btn{background:var(--green);color:var(--white);font-family:'Cinzel',serif;font-weight:600;display:flex;align-items:center;justify-content:center;border-radius:24px}
.hero-btn{left:89px;top:469px;width:197px;height:44px;font-size:15px}
.hero-photo{left:666px;top:159px;width:380px;height:380px;border-radius:50%;background:radial-gradient(circle at 45% 40%,#8aa04a,#4d6a25 55%,#2c3d18)}
.hero-seal{left:891px;top:388px;width:174px;height:174px;border-radius:50%;background:var(--white);border:6px solid var(--green);display:flex;align-items:center;justify-content:center;text-align:center;font-family:'Cinzel',serif;font-weight:700;font-size:20px;line-height:1.2;color:var(--green)}

/* about */
.about-card{left:158px;top:615px;width:884px;height:343px;background:var(--white);border-radius:12px;box-shadow:0 6px 30px rgba(0,0,0,.08)}
.about-photo{left:175px;top:634px;width:275px;height:306px;border-radius:8px;background:linear-gradient(135deg,#cfc6b4,#8b6a48 60%,#5a4a3a)}
.about-text{left:481px;top:650px;width:520px}
.eyebrow{font-weight:500;font-size:17px;color:var(--green)}
.about-heading{font-family:'Cinzel',serif;font-weight:700;font-size:27px;line-height:31px;color:var(--ink);margin-top:6px}
.about-copy{font-size:13.5px;line-height:19.6px;margin-top:10px;color:var(--ink)}
.tick-list{list-style:none;margin-top:8px}
.tick-list li{display:flex;align-items:center;gap:8px;font-size:14px;height:26.5px;color:var(--ink)}

/* services */
.section-title{width:1200px;left:0;text-align:center;font-family:'Cinzel',serif;font-weight:600;font-size:29px;color:var(--ink)}
.tab{font-family:'Cinzel',serif;font-weight:600;font-size:17px;transform:translateX(-50%);white-space:nowrap}
.product-card{width:373px;height:467px;top:1173px;background:var(--white);border-radius:12px;box-shadow:0 6px 26px rgba(0,0,0,.09);overflow:hidden}
.product-photo{width:100%;height:206px}
.product-rule{position:absolute;left:31px;top:234px;width:2px;height:137px;background:var(--green)}
.product-name{position:absolute;left:47px;top:236px;width:310px;font-family:'Cinzel',serif;font-weight:600;font-size:27px;line-height:31px;color:var(--ink)}
.product-desc{position:absolute;left:48px;top:304px;width:300px;font-size:14px;line-height:19.6px;color:var(--ink)}
.product-price{position:absolute;left:30px;top:400px;font-family:'Cinzel',serif;font-weight:600;font-size:18px;color:var(--ink)}
.product-cart{position:absolute;left:30px;top:430px;font-family:'Cinzel',serif;font-size:14px;color:var(--ink)}
.card-seal{left:552px;top:1246px;width:92px;height:92px;border-radius:50%;background:var(--white);border:4px solid var(--green);box-shadow:0 0 0 6px rgba(255,255,255,.7);display:flex;align-items:center;justify-content:center;font-family:'Cinzel',serif;font-weight:700;font-size:13px;color:var(--green);text-align:center}

/* cta band */
.cta-band{left:0;top:1724px;width:1200px;height:208px;background:radial-gradient(ellipse at 20% 10%,#17803d,var(--green) 60%)}
.cta-text{left:143px;top:1795px;font-family:'Cinzel',serif;font-weight:600;font-size:27px;line-height:31px;color:var(--white)}
.cta-btn{left:915px;top:1806px;width:141px;height:44px;background:var(--white);color:var(--green);font-size:14px}

/* case studies */
.case-photo{top:2091px;width:421px;height:260px;border-radius:12px}
.case-title{top:2382px;width:400px;font-family:'Cinzel',serif;font-weight:600;font-size:17px;line-height:21px;color:var(--ink)}
.case-copy{top:2428px;width:380px;font-size:13.5px;line-height:19.6px;color:var(--ink)}
.read-btn{left:536px;top:2650px;width:128px;height:45px;font-size:15px}

/* contact */
.contact-bg{left:0;top:2735px;width:1200px;height:579px;background:linear-gradient(100deg,#f7f0e6,#ffffff 45%,#f7f0e6)}
.contact-frame{left:369px;top:2826px;width:599px;height:408px;border:1.5px solid var(--green);border-radius:10px;background:var(--white)}
.contact-panel{left:230px;top:2871px;width:285px;height:325px;background:var(--green-bright);border-radius:8px;color:var(--white)}
.panel-heading{position:absolute;left:37px;font-family:'Cinzel',serif;font-weight:600;font-size:28px}
.panel-line{position:absolute;left:37px;top:85px;width:77px;height:1.5px;background:var(--white)}
.panel-row{position:absolute;left:37px;display:flex;align-items:center;gap:14px;font-size:11px;font-weight:500}
.social{position:absolute;top:259px;width:21px;height:21px;border-radius:50%;border:1.5px solid var(--white)}
.social.filled{background:var(--white)}
.touch-heading{left:558px;top:2890px;font-family:'Cinzel',serif;font-weight:600;font-size:28px;color:var(--ink)}
.touch-copy{left:559px;top:2934px;width:380px;font-size:14px;line-height:19.6px;color:var(--ink)}
.field-label{left:560px;font-size:10px;font-weight:500;color:var(--ink)}
.field-line{left:560px;width:316px;height:1px;background:#555}
.submit-btn{left:560px;top:3160px;width:129px;height:43px;font-size:15px}

/* footer */
.site-footer{left:0;top:3314px;width:1200px;height:283px;background:var(--green)}
.footer-brand{left:500px;top:3350px;width:200px;text-align:center;color:var(--white);font-family:'Cinzel',serif;font-weight:600;font-size:16px;line-height:1.3}
.footer-dot{width:60px;height:60px;margin:0 auto 8px;border-radius:50%;border:3px solid var(--white)}
.footer-nav{top:3489px;font-family:'Cinzel',serif;font-weight:600;font-size:18px;color:var(--white)}
.footer-sep{top:3488px;width:1px;height:26px;background:rgba(255,255,255,.45)}
.footer-rule{left:140px;top:3550px;width:922px;height:1px;background:rgba(255,255,255,.45)}
.copyright{left:0;width:1200px;top:3566px;text-align:center;font-size:10.5px;font-weight:500;color:var(--white)}
</style>
</head>
<body>

<!-- Header -->
<header class="abs site-header"></header>
<div class="abs brand-badge"><span class="brand-dot"></span><span class="brand-name">Edwin J.<br>Harrow</span></div>
<nav>
  <span class="abs main-nav" style="left:460px">Home</span>
  <span class="abs main-nav" style="left:539px">About</span>
  <span class="abs main-nav" style="left:624px">Services</span>
  <span class="abs main-nav" style="left:720px">Case Studies</span>
  <span class="abs main-nav" style="left:849px">Contact</span>
</nav>
<svg class="abs" style="left:936px;top:28px" width="100" height="16" viewBox="0 0 100 16" fill="none" stroke="#fff" stroke-width="1.5">
  <circle cx="7" cy="7" r="4.5"/><line x1="10.5" y1="10.5" x2="14" y2="14"/>
  <line x1="27" y1="1" x2="27" y2="15" stroke-opacity=".4"/>
  <circle cx="50" cy="5" r="3"/><path d="M44 14c1-4 11-4 12 0"/>
  <line x1="62" y1="1" x2="62" y2="15" stroke-opacity=".4"/>
  <path d="M78 3h3l2 8h8l2-6h-11"/><circle cx="84" cy="14" r="1"/><circle cx="90" cy="14" r="1"/>
</svg>
<div class="abs lang-pill">ENG <svg width="8" height="6" viewBox="0 0 8 6" fill="none" stroke="#fff" stroke-width="1.5"><path d="M1 1l3 3 3-3"/></svg></div>

<!-- Hero -->
<section>
  <div class="abs hero-bg"></div>
  <div class="abs hero-deco"></div>
  <span class="abs" style="left:29px;top:133px;width:7px;height:7px;border-radius:50%;background:var(--green)"></span>
  <p class="abs hero-kicker">Welcome to Edwin J. Harrow</p>
  <h1 class="abs hero-title">Your Family’s<br>Story Awaits</h1>
  <p class="abs hero-copy">Every family has a story. Every name carries a legacy. Start your journey today with expert genealogy research.</p>
  <a class="abs btn hero-btn">Start Your Journey</a>
  <svg class="abs" style="left:640px;top:115px" width="450" height="460" viewBox="0 0 450 460" fill="none" stroke="#0b6b2e" stroke-width="1.3">
    <circle cx="225" cy="235" r="213"/>
    <path d="M290 30a130 130 0 0 1 110 150" />
    <path d="M300 10a160 160 0 0 1 130 180" stroke-opacity=".6"/>
    <path d="M250 48a100 100 0 0 1 120 90" stroke-opacity=".5"/>
    <circle cx="399" cy="28" r="5" fill="#0b6b2e"/>
    <circle cx="292" cy="36" r="4" fill="#fff"/>
    <circle cx="72" cy="91" r="5" fill="#fff" stroke="#e0b75a"/>
    <circle cx="408" cy="141" r="3" fill="#fff" stroke="#e0b75a"/>
  </svg>
  <div class="abs hero-photo" role="img" aria-label="Child sitting on a moss-covered tree in a green forest, looking upward"></div>
  <div class="abs hero-seal">Edwin J.<br>Harrow</div>
</section>

<!-- About -->
<section>
  <div class="abs about-card"></div>
  <div class="abs about-photo" role="img" aria-label="Genealogist reading an old family book with children at a table"></div>
  <div class="abs about-text">
    <p class="eyebrow">ABOUT US</p>
    <h2 class="about-heading">Meet Edwin J. Harrow<br>Your Family History Specialist</h2>
    <p class="about-copy">Edwin J. Harrow is passionate about uncovering family stories. With years of experience in genealogy research, he has helped hundreds of families reconnect with their heritage. Whether through traditional records or cutting-edge DNA analysis, every family has a unique history waiting to be discovered.</p>
    <ul class="tick-list">
      <li><svg width="13" height="13" viewBox="0 0 13 13"><circle cx="6.5" cy="6.5" r="6.5" fill="#0b6b2e"/><path d="M3.5 6.7l2 2 4-4" stroke="#fff" stroke-width="1.6" fill="none"/></svg>Expert in historical records research</li>
      <li><svg width="13" height="13" viewBox="0 0 13 13"><circle cx="6.5" cy="6.5" r="6.5" fill="#0b6b2e"/><path d="M3.5 6.7l2 2 4-4" stroke="#fff" stroke-width="1.6" fill="none"/></svg>Specialist in DNA ancestry tracing</li>
      <li><svg width="13" height="13" viewBox="0 0 13 13"><circle cx="6.5" cy="6.5" r="6.5" fill="#0b6b2e"/><path d="M3.5 6.7l2 2 4-4" stroke="#fff" stroke-width="1.6" fill="none"/></svg>Helping Australians connect with their past</li>
    </ul>
  </div>
</section>

<!-- Products & Services -->
<section>
  <h2 class="abs section-title" style="top:1056px">Products &amp; Services</h2>
  <span class="abs tab" style="left:404px;top:1136px;color:var(--ink)">Traditional Genealogy Research</span>
  <span class="abs tab" style="left:778px;top:1136px;color:var(--muted)">DNA-Based Ancestry Tracing</span>

  <article class="abs product-card" style="left:215px">
    <div class="product-photo" role="img" aria-label="Parents greeting their young children outdoors in autumn" style="background:linear-gradient(160deg,#c9c1a6,#7d6a4d 60%,#4e4436)"></div>
    <span class="product-rule"></span>
    <h3 class="product-name">Basic Family Tree Package</h3>
    <p class="product-desc">We research and provide a 3-generation family tree based on available records. (Delivery: Digital report &amp; family chart)</p>
    <p class="product-price">Price: AUD 199</p>
    <p class="product-cart">Add to Cart</p>
  </article>
  <article class="abs product-card" style="left:606px">
    <div class="product-photo" role="img" aria-label="Father and son exploring with binoculars in an open field" style="background:linear-gradient(160deg,#e2e2de,#b08a5a 60%,#6d5a40)"></div>
    <span class="product-rule"></span>
    <h3 class="product-name">Advanced Family History Package</h3>
    <p class="product-desc">Full research covering up to 6 generations, including detailed reports, documents, and historical narratives. (Delivery: Digital + optional printed book)</p>
    <p class="product-price">Price: AUD 499</p>
    <p class="product-cart">Add to Cart</p>
  </article>
  <div class="abs card-seal">Harrow</div>
</section>

<!-- Call to action band -->
<section>
  <div class="abs cta-band"></div>
  <p class="abs cta-text">Need a Custom Research Plan?<br>Contact us for a personalized package!</p>
  <a class="abs btn cta-btn">Contact us</a>
</section>

<!-- Case Studies -->
<section>
  <h2 class="abs section-title" style="top:2028px">Case Studies</h2>
  <div class="abs case-photo" style="left:168px;background:linear-gradient(150deg,#cfc4b6,#8a8478 50%,#3f5a52)" role="img" aria-label="Grandmother and two children examining nature with a magnifying glass"></div>
  <div class="abs case-photo" style="left:606px;background:linear-gradient(160deg,#3f5530,#2d3b24 55%,#6a6a52)" role="img" aria-label="Group in traditional folk costumes dancing outdoors"></div>
  <h3 class="abs case-title" style="left:168px">Margaret’s Scottish Heritage Uncovered</h3>
  <p class="abs case-copy" style="left:168px">Margaret had always believed she was connected to a historic Scottish clan but lacked any official proof. Through meticulous genealogical research, we traced her family’s origins back to a 17th-century Scottish settlement. Armed with historical documentation and verified lineage, she was able to gain recognition from the clan society, solidifying her place in history and strengthening her family legacy.</p>
  <h3 class="abs case-title" style="left:606px">John’s Lost Family Found Through DNA</h3>
  <p class="abs case-copy" style="left:606px">John had always wondered about his grandfather, a man he had only heard stories about but never met. With no official records to trace his lineage, he turned to our DNA-based ancestry service. Through genetic matching and historical records, we uncovered a network of relatives in Ireland, reconnecting John with long-lost family members. The journey not only provided him with answers but also led to an emotional reunion that reshaped his understanding of his roots.</p>
  <a class="abs btn read-btn">Read More</a>
</section>

<!-- Contact -->
<section>
  <div class="abs contact-bg"></div>
  <div class="abs contact-frame"></div>
  <div class="abs contact-panel">
    <h2 class="panel-heading" style="top:40px">Contact Us</h2>
    <span class="panel-line"></span>
    <div class="panel-row" style="top:118px">
      <svg width="12" height="12" viewBox="0 0 24 24" fill="#fff"><path d="M6.6 10.8a15 15 0 0 0 6.6 6.6l2.2-2.2c.3-.3.7-.4 1-.2 1.1.4 2.3.6 3.6.6.6 0 1 .4 1 1V20c0 .6-.4 1-1 1A17 17 0 0 1 3 4c0-.6.4-1 1-1h3.5c.6 0 1 .4 1 1 0 1.3.2 2.5.6 3.6.1.3 0 .7-.2 1z"/></svg>( 321 ) 555-0148</div>
    <div class="panel-row" style="top:166px">
      <svg width="12" height="10" viewBox="0 0 24 20" fill="#fff"><path d="M2 0h20a2 2 0 0 1 2 2v16a2 2 0 0 1-2 2H2a2 2 0 0 1-2-2V2a2 2 0 0 1 2-2zm10 11L2 4v2l10 7 10-7V4z"/></svg>INFO@HARROWHISTORY.TEST</div>
    <h2 class="panel-heading" style="top:215px">Follow Us</h2>
    <span class="social" style="left:37px"></span>
    <span class="social filled" style="left:68px"></span>
    <span class="social" style="left:98px"></span>
    <span class="social" style="left:129px"></span>
  </div>
  <h2 class="abs touch-heading">Get in Touch</h2>
  <p class="abs touch-copy">Have questions? Ready to start your family research journey? Get in touch today!</p>
  <span class="abs field-label" style="top:2999px">NAME</span><span class="abs field-line" style="top:3018px"></span>
  <span class="abs field-label" style="top:3045px">E-MAIL</span><span class="abs field-line" style="top:3065px"></span>
  <span class="abs field-label" style="top:3112px">MESSAGE</span><span class="abs field-line" style="top:3132px"></span>
  <a class="abs btn submit-btn">Submit</a>
</section>

<!-- Footer -->
<footer>
  <div class="abs site-footer"></div>
  <div class="abs footer-brand"><div class="footer-dot"></div>Edwin J. Harrow</div>
  <span class="abs footer-nav" style="left:308px">Home</span>
  <span class="abs footer-sep" style="left:385px"></span>
  <span class="abs footer-nav" style="left:408px">About</span>
  <span class="abs footer-sep" style="left:492px"></span>
  <span class="abs footer-nav" style="left:516px">Services</span>
  <span class="abs footer-sep" style="left:616px"></span>
  <span class="abs footer-nav" style="left:640px">Case Studies</span>
  <span class="abs footer-sep" style="left:786px"></span>
  <span class="abs footer-nav" style="left:806px">Contact</span>
  <span class="abs footer-rule"></span>
  <p class="abs copyright">2024 EDWIN J. HARROW. ALL RIGHTS RESERVED.</p>
</footer>

</body>
</html>
```